Glow in the Dark Inks Sales Flyer - Targeted to the music industry

We need help!
We need a creative flyer to tell the music industry about our new, colorful glow in the dark inks that look amazing on T-shirts and concert merchandise.

The flyer will go to merchandising managers for bands around the world. The design needs to be hip and contemporary but not offensive. No f-bombs please! Size is 4” x 6” or 3” x 5”, and will be printed on card stock. Design can be both sides if you want. We expect color but black and white with some fluorescent accents could be cool. Surprise us.
Here’s some copy, and we can fill in the contact info when the design is close to final.

Help your fans get lit with branded T-shirts and merchandise that glows in the dark!

Let our new Starwell Inks light up your next show!

Call us now –
Updates

Hello Designers.

Please keep in mind that although the thought of glow-in-the-dark may trigger a glowing, green color in your creative minds, StarWell Inks has a wide variety of colors to bring to offer. So please be sure to show that it's not only green glow we are promoting but we have a wide range of colors that glow (including pink, purple, white that glow blue, blue, green, orange, yellow, etc.)

Thank you!

```html
<!DOCTYPE html>
<html lang="en">
<head>
<meta charset="utf-8">
<title>Glow Inks Flyer</title>
<link rel="stylesheet" href="https://fonts.googleapis.com/css2?family=Arimo:wght@400;700&family=Open+Sans:wght@400&display=swap">
<style>
  :root {
    --page: #ffffff;
    --card-black: #060606;
    --figure-dark: #1c1c1c;
    --glow-cyan: #33c1dc;
    --glow-lime: #cfe03f;
    --glow-amber: #b9863a;
    --title-teal: #6cc3a6;
    --title-mint: #e3f3ea;
    --title-pink: #d0417f;
    --body-white: #ffffff;
    --outline: #1b1b1b;
    --info-grey: #6d6e71;
    --info-border: #8a6c52;
  }
  * { margin: 0; padding: 0; box-sizing: border-box; }
  html, body { width: 1200px; height: 1098px; overflow: hidden; background: var(--page); }
  .canvas { position: relative; width: 1200px; height: 1098px; }

  .card {
    position: absolute; top: 288px; width: 432px; height: 648px;
    background: var(--card-black); overflow: hidden;
  }
  .card--front { left: 144px; }
  .card--back { left: 597px; }

  .front-art {
    position: absolute; left: 40px; top: 0; width: 392px; height: 648px;
    background:
      radial-gradient(ellipse 70px 190px at 230px 470px, var(--glow-lime) 0%, #9fbf4a 45%, var(--glow-amber) 75%, transparent 100%),
      radial-gradient(ellipse 160px 90px at 250px 170px, rgba(51,193,220,0.85) 0%, rgba(51,193,220,0.25) 60%, transparent 100%),
      radial-gradient(ellipse 60px 200px at 370px 330px, rgba(51,193,220,0.7) 0%, transparent 100%),
      linear-gradient(160deg, var(--figure-dark) 0%, #141414 55%, var(--card-black) 100%);
  }

  .front-title {
    position: absolute; left: 18px; top: 44px;
    font-family: "Open Sans", sans-serif; font-size: 76px; font-weight: 400;
    letter-spacing: 1px; transform: rotate(-8deg); transform-origin: left bottom;
    background: linear-gradient(90deg, var(--title-teal), var(--title-mint));
    -webkit-background-clip: text; background-clip: text; color: transparent;
  }

  .back-art {
    position: absolute; inset: 0;
    background:
      radial-gradient(ellipse 120px 160px at 30px 140px, rgba(51,193,220,0.75), transparent 100%),
      radial-gradient(ellipse 180px 90px at 330px 40px, rgba(51,193,220,0.7), transparent 100%),
      radial-gradient(ellipse 90px 200px at 420px 300px, rgba(51,193,220,0.65), transparent 100%),
      radial-gradient(ellipse 100px 180px at 60px 560px, rgba(51,193,220,0.6), transparent 100%),
      radial-gradient(ellipse 110px 80px at 220px 620px, rgba(51,193,220,0.55), transparent 100%),
      var(--card-black);
  }

  .back-title {
    position: absolute; left: 24px; top: 30px;
    font-family: "Open Sans", sans-serif; font-size: 56px; font-weight: 400;
    white-space: nowrap; transform: rotate(-6deg); transform-origin: left bottom;
    background: linear-gradient(90deg, var(--title-pink) 0%, var(--title-pink) 48%, var(--title-teal) 70%, var(--title-mint) 100%);
    -webkit-background-clip: text; background-clip: text; color: transparent;
  }

  .pitch {
    position: absolute; left: 0; top: 122px; width: 432px;
    text-align: center; font-family: "Arimo", sans-serif; font-weight: 700;
    font-size: 31px; line-height: 37px; letter-spacing: 1px;
    color: var(--body-white);
    -webkit-text-stroke: 1px var(--outline);
    text-shadow: 2px 2px 0 var(--outline), -1px -1px 0 var(--outline);
  }

  .company-info {
    position: absolute; left: 28px; top: 528px; width: 388px; height: 96px;
    background: var(--info-grey); border: 4px dashed var(--info-border);
    display: flex; align-items: center; justify-content: center;
    font-family: "Arimo", sans-serif; font-size: 27px; color: #000;
  }
</style>
</head>
<body>
<main class="canvas">
  <section class="card card--front">
    <div class="front-art" role="img" aria-label="Illustration of a dancer silhouette lit in glowing cyan with a yellow-green glow streak"></div>
    <h1 class="front-title">glow!</h1>
  </section>

  <section class="card card--back">
    <div class="back-art" role="img" aria-label="Cyan glow paint splatter across a black background"></div>
    <h2 class="back-title">rules the night</h2>
    <p class="pitch">You need shirts<br>SURPRISING<br>to blow up colors,<br>even at NIGHT!.<br>Amazing for promote<br>your concert or event.<br>We have a wide<br>variety of&nbsp; glow inks,<br>just bring us your<br>design.</p>
    <div class="company-info">COMPANY INFO</div>
  </section>
</main>
</body>
</html>
```